Designing a new homepage for www.Pelmora.net

WEBSITE: www.pelmora.net

ABOUT THE WEBSITE
The Pelmora.net (PLM) website contains a large directory of over 50,000 international trade service providers that is not valued enough on the homepage (HP). Currently from the HP, the site appears as a general site about imports and exports (international trade). As a result, it contradicts the purpose and experience of the site.
The website is new and original for international trade online: it is a tool to find the best experts and professionals that can help importers and exporters to implement their overseas operations.

Specifically:
a) An exporter who wants to sell in Italy can find on PLM: agents to distribute their products, a lawyer for reviewing contracts, translators to translate brochures and websites, an export consultant, etc. Various local providers that can help sell their products in Italy, a local provider (e.g. based in Italy) are generally more efficient and less costly than a supplier in the exporter’s home country

b) An importer who wants to buy in China will find purchasing agents who source products for third parties; logistics companies that store and ship merchandise; corporate quality control to ensure product quality before shipment, etc.; various local providers based in China to better organize its import operation.

PLM is therefore a very resourceful solution for SMEs who want to develop, improve and organize their international trade:
a) it significantly increases their ability to create new opportunities by using the services of a third party: export to a new country; import a new product
b) it allows them to optimize their purchases of services by seeking alternatives: find a less expensive carrier, a foreign lawyer challenged by a local lawyer

It is the perfect complement to cross border marketplaces (e.g. Vuxentor.com, brimwellhub.com, zq48.com) which concentrate on the search for products (and of companies/counterparts) but:
a) help the user to import only, not really export
b) do not help implement the operations of exporting/importing from A to Z

Therefore, PLM offers a new way of “easy exporting” (or easy importing).

THE BRIEF

The objective of the project is to rethink the HP (and the site design) to highlight this experience: "export and import more successfully through 50,000+ service providers in over 100 countries”.
We have created a wireframe (see attached) of the structure we feel best meets this objective. What do you think? Do we meet it through our wireframe? Then, next step is to take this wireframe and create a clear design that really helps us to achieve our objective.

It is considered that the site captures the importers/exporters seeking to increase their exports or to better organize their imports (but we do not start from a priori that these users are looking for service providers).
The HP should highlight the importance of service providers addressing export markets or better organizing their imports; the "market analyses" of the site should act as a "knowledge resource", where the site offers more the main experience: if you want to export to a country you have any interest to first explore what the partners listed by PLM can provide.

Reason: We feel that we're seeing some interesting designs and would like to give current and even potential submissions more time. So far we have not seen the one that really strikes us, so perhaps more time is what we and the designers need! Thanks!

Target Market(s)

Importers, exporters, international trade service providers, foreign investors, etc

Industry/Entity Type

Lawyer

Requirements
Must have
• • Please use the current basic design elements of the website, including the logo, (www.pelmora.net). These include colors and fonts, etc. We only aim to change the HP and therefore, only implement a change to the header and footer of the whole site.
• Please find inspiration from our wireframes (attached), as they have been carefully thought about by our own team. However, should you feel the need to challenge the wireframes, please do so in your design, we're interested to see what you can present us.
• Our prime objective in terms of design: creating a more user-friendly interface on the HP to guide users into the rest of the website
• We already have a psd file based on the wireframes we’ve attached to the brief. If you would like this, so your job is easier (such as using same text as we have in the wireframes), let us know!

```html
<!DOCTYPE html>
<html lang="en">
<head>
<meta charset="utf-8">
<title>Pelmora.net – The Network for International Trade Services</title>
<link href="https://fonts.googleapis.com/css2?family=Roboto:ital,wght@0,400;0,500;0,700;1,400&family=Roboto+Condensed:wght@700&display=swap" rel="stylesheet">
<style>
:root{
  --blue:#1b8fd2;
  --blue-dark:#0e4f86;
  --blue-head:#2583c6;
  --link:#1b78c2;
  --text:#333;
  --muted:#666;
  --line:#d8d8d8;
  --bg-soft:#f2f2f2;
  --footer:#ececec;
  --white:#fff;
}
*{box-sizing:border-box;margin:0;padding:0}
html,body{width:1200px;height:2646px;overflow:hidden}
body{position:relative;background:var(--white);font-family:"Roboto",Arial,sans-serif;color:var(--text);font-size:14px}
a{color:inherit;text-decoration:none}
ul{list-style:none}
.abs{position:absolute}

/* top bar */
.topbar{left:0;top:0;width:1200px;height:46px;border-bottom:1px solid var(--line);background:#fafafa}
.topbar .main-nav{left:38px;top:0;height:46px;display:flex;align-items:center;font-size:15px;color:var(--link)}
.topbar .main-nav a{padding:0 22px;border-left:1px solid #bbb;line-height:16px}
.topbar .main-nav a:first-child{padding-left:0;border:0}
.topbar .user-nav{right:50px;top:0;height:46px;display:flex;font-size:14px;color:#444}
.topbar .user-nav a{display:flex;align-items:center;padding:0 24px;border-left:1px solid var(--line)}

/* logo */
.brand{left:28px;top:92px}
.brand-name{font-size:40px;font-weight:700;color:var(--blue-dark);letter-spacing:3px;line-height:44px}
.brand-tag{font-size:13px;color:#444;margin-left:118px}

/* header card */
.header-card{left:21px;top:180px;width:1158px;height:392px;border:1px solid var(--line)}
.section-nav{left:0;top:0;width:1156px;height:60px;background:#f6f6f6;border-bottom:1px solid var(--line);display:flex;align-items:center;font-size:16px;color:var(--link)}
.section-nav a{margin-left:28px;margin-right:20px}
.search{right:18px;top:12px;width:422px;height:36px;border:1px solid var(--line);background:var(--white);font-size:13px;color:#555;padding:9px 12px}
.search svg{position:absolute;right:10px;top:9px}
.hero-title{left:30px;top:90px;font-family:"Roboto Condensed",Arial,sans-serif;font-weight:700;font-size:47px;color:var(--blue-head);letter-spacing:-0.5px}
.hero-sub{left:30px;top:154px;font-size:22px;font-weight:500;color:var(--blue)}
.hero-list{left:36px;top:200px;font-size:16px;color:#222;line-height:35px}
.hero-list li::before{content:"";display:inline-block;width:8px;height:8px;border-radius:50%;background:#111;margin-right:14px;vertical-align:middle}
.hero-listed{left:55px;top:322px;font-size:15px;color:var(--blue)}
.badge{background:#bdbdbd;border:1px solid #999}
.hero-art{left:762px;top:74px;width:360px;height:306px;border-radius:4px;background:linear-gradient(180deg,#d6e9f7 0%,#b8d8f0 55%,#eef3f7 100%)}

/* start band */
.start-band{left:21px;top:575px;width:1158px;height:81px;background:var(--blue)}
.start-band .lead{left:30px;top:20px;font-family:"Roboto Condensed",Arial,sans-serif;font-weight:700;font-size:30px;color:var(--white)}
.country-select{left:176px;top:20px;width:300px;height:42px;background:var(--white);color:var(--blue-dark);font-size:16px;font-weight:500;padding:11px 16px}
.country-select .caret{position:absolute;right:0;top:0;width:42px;height:42px;border-left:1px solid var(--line);display:flex;align-items:center;justify-content:center}
.start-band .assist{left:500px;top:31px;color:var(--white);font-size:16px}
.check{top:26px;color:var(--white);font-size:22px;display:flex;align-items:center}
.check i{display:inline-block;width:24px;height:24px;background:var(--white);margin-right:10px}
.go{left:1070px;top:12px;width:56px;height:56px;border-radius:50%;background:var(--blue-dark);color:var(--white);font-size:24px;font-weight:500;display:flex;align-items:center;justify-content:center}

/* country feature */
.feature{left:21px;top:673px;width:1158px;height:241px;border:1px solid var(--line);background:var(--white);box-shadow:0 1px 3px rgba(0,0,0,.12)}
.feature .arrow{top:18px}
.feature-title{left:76px;top:14px;font-size:30px;color:var(--blue-head);font-weight:400}
.feature-discover{left:600px;top:24px;font-size:16px;color:#555}
.feature-rule{left:18px;top:66px;width:1120px;height:1px;background:var(--line)}
.provider-logo{left:36px;top:90px;width:96px;height:96px;border:1px solid var(--line);border-radius:4px}
.provider-logo span{position:absolute;left:14px;top:14px;width:66px;height:66px;border-radius:50%;background:#d9d9d9}
.provider-name{left:156px;top:92px;font-size:18px;color:#222}
.provider-role{left:156px;top:115px;font-size:14px;color:#444}
.provider-desc{left:156px;top:142px;width:360px;font-size:13px;color:#555;line-height:18px}
.provider-url{left:156px;top:200px;font-size:12px;color:#444}
.provider-cta{left:388px;top:200px;font-size:12px;color:#444}
.feature-split{left:546px;top:80px;width:1px;height:140px;background:var(--line)}
.stat{top:90px;width:160px;text-align:center;color:#555;font-size:14px;line-height:18px}
.stat b{display:block;font-size:48px;font-weight:400;color:#333;line-height:56px}
.stat a{text-decoration:underline;color:#555}

/* columns */
.col-head{font-size:18px;font-weight:400;color:var(--blue-head);padding-bottom:10px;border-bottom:2px solid #e3eef8}
.directory{left:21px;top:937px;width:302px}
.dir-box{margin-top:16px;border:1px solid var(--line);height:1090px;position:relative}
.dir-tabs{display:flex;height:44px}
.dir-tabs div{flex:1;display:flex;align-items:center;justify-content:center;font-size:15px;color:#444;background:#e7e7e7;border-bottom:1px solid var(--line)}
.dir-tabs .active{background:var(--white);border:1px solid var(--line);border-bottom:0;margin:8px 0 0 14px;flex:none;width:126px}
.dir-list{padding:10px 0 0 20px;font-size:13px;color:#444;line-height:29.4px}
.dir-list li::before{content:"";display:inline-block;width:5px;height:5px;background:var(--blue);margin-right:14px;vertical-align:middle}

.says{left:345px;top:937px;width:417px;height:1140px}
.quote-photo{width:117px;height:105px;border:1px solid var(--line);background:linear-gradient(160deg,#e8d8c8,#c9a98e 60%,#9a7d68)}
.quote-name{left:134px;top:12px;font-size:15px;color:#222;line-height:20px}
.quote-name small{display:block;font-size:13px;color:#555}
.quote-text{font-size:12.5px;font-style:italic;color:#555;line-height:19px}
.btn{background:var(--blue);color:var(--white);font-family:"Roboto Condensed",Arial,sans-serif;font-weight:700;font-size:17px;display:flex;align-items:center;justify-content:center;border:1px solid #1076b4}
.small-link{font-size:13px;color:#333;text-decoration:underline}
.tip-title{font-size:15px;color:#222;font-weight:500}
.tip-text{font-size:13.5px;font-weight:500;color:#222;line-height:22px;margin-top:8px}
.tip-text b{font-weight:700}
.stars{display:flex;align-items:center;gap:3px;font-size:12px;color:#333}

.newsp{left:793px;top:937px;width:386px;height:700px}
.np-photo{width:110px;height:105px;border:1px solid var(--line);background:linear-gradient(150deg,#f1e3d6,#d8bfaa 55%,#a9b1ba)}
.np-name{left:122px;top:0;font-size:14px;color:#222;line-height:20px;font-weight:500}
.np-name span{display:block;font-size:16px}
.np-desc{left:122px;top:44px;width:262px;font-size:12.5px;color:#555;line-height:17px}
.np-more{right:0;top:90px;font-size:12px;color:#444;text-decoration:underline}

.knowledge{left:793px;top:1648px;width:386px}
.k-intro{font-size:14px;color:var(--blue);font-weight:500;margin-top:14px}
.k-list{margin-top:14px;font-size:14px;color:#222;line-height:24px;padding-left:8px}
.k-list li::before{content:"•";margin-right:14px}
.k-list b{display:inline-block;width:54px;font-weight:400}
.k-select{margin-top:6px;display:flex;gap:10px}
.k-select .box{width:296px;height:30px;border:1px solid #bbb;background:linear-gradient(#fff,#eee);font-size:13px;color:#444;padding:6px 10px;position:relative}
.k-select .box::after{content:"▾";position:absolute;right:8px;top:5px;color:#555}
.k-select .ok{width:34px;height:30px;background:var(--blue);color:var(--white);font-size:13px;display:flex;align-items:center;justify-content:center}
.k-pop{margin-top:20px;font-size:13px;color:#333}
.k-countries{margin-top:12px;font-size:13.5px;color:#444;line-height:23px}

/* partners */
.partners{left:21px;top:2098px;width:1158px;height:120px;border-top:1px solid var(--line);display:flex;align-items:center;justify-content:space-between;padding:0 10px}
.partner{height:60px;background:#bfbfbf}

/* footer */
.footer{left:0;top:2240px;width:1200px;height:406px;background:var(--footer)}
.foot-col{top:56px}
.foot-col h4{font-size:16px;font-weight:400;color:var(--blue);margin-bottom:14px}
.foot-col li{font-size:12.5px;color:#444;line-height:29.5px}
.social li{display:flex;align-items:center;line-height:38px;font-size:14px}
.social i{display:inline-block;width:26px;height:26px;background:var(--blue);border-radius:3px;margin-right:14px}
.foot-rule{left:32px;top:330px;width:1136px;height:1px;background:#cfcfcf}
.copyright{left:34px;top:350px;font-size:12px;color:#444}
</style>
</head>
<body>

<header class="abs topbar">
  <nav class="abs main-nav"><a href="#">Home</a><a href="#">About us</a><a href="#">Take a tour</a><a href="#">Advertise</a><a href="#">Why Pelmora.net</a></nav>
  <nav class="abs user-nav"><a href="#">LOGIN</a><a href="#">SIGN UP</a><a href="#">LIST YOUR SERVICES</a></nav>
</header>

<div class="abs brand">
  <div class="brand-name">PELMORA.net</div>
  <div class="brand-tag">The Network for International Trade Services</div>
</div>

<section class="abs header-card">
  <nav class="abs section-nav"><a href="#">ALL TRADE SERVICES</a><a href="#" style="margin-left:60px">LET US HELP YOU</a><a href="#" style="margin-left:60px">BROWSE KNOWLEDGE</a></nav>
  <div class="abs search">Search 20,000 + content itmes &amp; 50,000 + service providers
    <svg width="16" height="16" viewBox="0 0 16 16"><circle cx="6.5" cy="6.5" r="5" fill="none" stroke="#999" stroke-width="2"/><line x1="10" y1="10" x2="15" y2="15" stroke="#999" stroke-width="2"/></svg>
  </div>
  <h1 class="abs hero-title">Improve your business overseas!</h1>
  <p class="abs hero-sub">Use the leverage of 51,000+ verified serivces providers:</p>
  <ul class="abs hero-list">
    <li>Sales agents, market entry, customs services</li>
    <li>Sourcing companies, freight forwarders, quality control</li>
    <li>Lawyers, accounting, expat services and more</li>
  </ul>
  <p class="abs hero-listed">Includes the service providers listed by :</p>
  <div class="abs badge" style="left:378px;top:308px;width:50px;height:50px"></div>
  <div class="abs hero-art" role="img" aria-label="Illustration of a globe with currency symbols"></div>
</section>

<section class="abs start-band">
  <div class="abs lead">Start now</div>
  <div class="abs country-select">Select your target country
    <span class="caret"><svg width="14" height="9" viewBox="0 0 14 9"><path d="M0 0h14L7 9z" fill="#1b8fd2"/></svg></span>
  </div>
  <div class="abs assist">and find assistance to</div>
  <label class="abs check" style="left:700px"><i></i>Import</label>
  <label class="abs check" style="left:828px"><i></i>Export</label>
  <label class="abs check" style="left:946px"><i></i>Invest</label>
  <a class="abs go" href="#">Go</a>
</section>

<section class="abs feature">
  <svg class="abs arrow" style="left:30px" width="18" height="28" viewBox="0 0 18 28"><path d="M16 0v28L0 14z" fill="#2583c6"/></svg>
  <svg class="abs arrow" style="left:1112px" width="18" height="28" viewBox="0 0 18 28"><path d="M2 0v28l16-14z" fill="#888"/></svg>
  <h2 class="abs feature-title">Want to export to South Africa ?</h2>
  <p class="abs feature-discover">Discover 451 Services Providers to help you export including</p>
  <div class="abs feature-rule"></div>
  <div class="abs provider-logo"><span></span></div>
  <div class="abs provider-name">Korvale South Africa</div>
  <div class="abs provider-role">Export support</div>
  <p class="abs provider-desc">Brightmesh eSolutions is a professional website design company dedicated to provide excellent services.</p>
  <div class="abs provider-url">www.korvale.com</div>
  <div class="abs provider-cta">Want your logo here?</div>
  <div class="abs feature-split"></div>
  <div class="abs stat" style="left:593px"><b>25</b>Freight Forwarders<br>in South Africa<br><a href="#">See all</a></div>
  <div class="abs stat" style="left:781px"><b>47</b>Corporate Lawyers<br>in South Africa<br><a href="#">See all</a></div>
  <div class="abs stat" style="left:957px"><b>56</b>Debt Collectors<br>in South Africa<br><a href="#">See all</a></div>
</section>

<aside class="abs directory">
  <h3 class="col-head">Browse Our Directory</h3>
  <div class="dir-box">
    <div class="dir-tabs"><div class="active">Services 200+</div><div>Countries 100+</div></div>
    <ul class="dir-list">
      <li>Freight Forwarders</li><li>Trading Companies</li><li>Corporate Law</li><li>Investment Promotion</li><li>Distributors</li><li>Translation</li><li>Debt Collection</li><li>Accounting Services</li><li>Expat Services</li><li>Market Research</li><li>Debt Collection</li><li>Freight Forwarders</li><li>Trading Companies</li><li>Corporate Law</li><li>Investment Promotion</li><li>Distributors</li><li>Translation</li><li>Debt Collection</li><li>Accounting Services</li><li>Expat Services</li><li>Market Research</li><li>Debt Collection</li><li>Freight Forwarders</li><li>Trading Companies</li><li>Investment Promotion</li><li>Distributors</li><li>Translation</li><li>Debt Collection</li><li>Accounting Services</li><li>Expat Services</li><li>Market Research</li><li>Debt Collection</li><li>Freight Forwarders</li><li>Trading Companies</li>
    </ul>
  </div>
</aside>

<section class="abs says">
  <h3 class="col-head">What Importers / Exporters Say</h3>
  <div class="abs" style="left:6px;top:58px;width:411px">
    <div class="quote-photo" role="img" aria-label="Portrait photo of a customer"></div>
    <div class="abs quote-name">Name of Speaker<small>Sourcing Services<br>Florida, The United States</small></div>
    <p class="quote-text" style="margin-top:18px">E-Commerce is a major progress in technology that has changed the way in which the customers now purchase information, products and the services. It's the new way of providing an opportunity to make your products and services available in the global market 24 hours a day through Internet<br>Brightmesh eSolutions is specialized in handling advanced web projects and the ongoing projects that require permanent maintenance and support .We like challenges and do complete these challenge with expertise we like solving questions that arises in such</p>
  </div>
  <div class="abs" style="left:6px;top:390px;width:411px">
    <div class="quote-photo" role="img" aria-label="Portrait photo of a customer"></div>
    <div class="abs quote-name">Name of Speaker<small>Sourcing Services<br>Florida, The United States</small></div>
    <p class="quote-text" style="margin-top:14px">E-Commerce is a major progress in technology that has changed the way in which the customers now purchase information, products and the services. It's the new way of providing an opportunity to make your products and services available in the global market 24 hours a day through Internet</p>
  </div>
  <a class="abs small-link" href="#" style="left:6px;top:640px">See the benifits</a>
  <a class="abs btn" href="#" style="left:252px;top:629px;width:154px;height:36px">JOIN FOR FREE</a>

  <h3 class="abs col-head" style="top:710px;width:417px">Business Tips By Experts</h3>
  <div class="abs" style="left:0;top:758px;width:417px">
    <div class="tip-title">Business adminstration</div>
    <p class="tip-text">It's the new way of providing an opportunity to make your<br><b>a law update</b> by Lorem Ipsum</p>
    <div class="stars" style="margin:4px 0 0 264px"><svg width="94" height="16" viewBox="0 0 94 16"><g fill="#2a8ad0"><path id="st" d="M8 0l2.4 5 5.6.6-4.2 3.8 1.2 5.6L8 12.2 3 15l1.2-5.6L0 5.6 5.6 5z"/><use href="#st" x="19"/><use href="#st" x="38"/><use href="#st" x="57"/></g><use href="#st" x="76" fill="#ccc"/></svg><span style="margin-left:8px">Rated</span></div>
  </div>
  <div class="abs" style="left:0;top:870px;width:417px">
    <div class="tip-title">Business adminstration</div>
    <p class="tip-text">It's the new way of providing an opportunity to make your<br><b>a law update</b> by Lorem Ipsum</p>
    <div class="stars" style="margin:4px 0 0 264px"><svg width="94" height="16" viewBox="0 0 94 16"><g fill="#2a8ad0"><use href="#st"/><use href="#st" x="19"/><use href="#st" x="38"/><use href="#st" x="57"/></g><use href="#st" x="76" fill="#ccc"/></svg><span style="margin-left:8px">Rated</span></div>
  </div>
  <div class="abs" style="left:0;top:982px;width:417px">
    <div class="tip-title">Business adminstration</div>
    <p class="tip-text">It's the new way of providing an opportunity to make your<br><b>a law update</b> by Lorem Ipsum</p>
    <div class="stars" style="margin:4px 0 0 264px"><svg width="94" height="16" viewBox="0 0 94 16"><g fill="#2a8ad0"><use href="#st"/><use href="#st" x="19"/><use href="#st" x="38"/><use href="#st" x="57"/></g><use href="#st" x="76" fill="#ccc"/></svg><span style="margin-left:8px">Rated</span></div>
  </div>
  <a class="abs small-link" href="#" style="left:0;top:1104px">Browse all content</a>
  <a class="abs btn" href="#" style="left:243px;top:1097px;width:165px;height:34px">RECEIVE UPDATES</a>
</section>

<aside class="abs newsp">
  <h3 class="col-head">New Services Providers</h3>
  <div class="abs" style="left:6px;top:49px;width:380px;height:110px">
    <div class="np-photo" role="img" aria-label="Photo of provider representative"></div>
    <div class="abs np-name">Tenwick Media Limited<span>Tax services in the United Kingdom</span></div>
    <p class="abs np-desc">We here modify the site to improve the ranking by using the keywords contents.</p>
    <a class="abs np-more" href="#">view profile</a>
  </div>
  <div class="abs" style="left:6px;top:189px;width:380px;height:110px">
    <div class="np-photo" role="img" aria-label="Photo of a business team at work"></div>
    <div class="abs np-name">Tenwick Media Limited<span>Tax services in the United Kingdom</span></div>
    <p class="abs np-desc">We here modify the site to improve the ranking by using the keywords contents.</p>
    <a class="abs np-more" href="#">view profile</a>
  </div>
  <div class="abs" style="left:6px;top:328px;width:380px;height:110px">
    <div class="np-photo" role="img" aria-label="Photo of provider representative"></div>
    <div class="abs np-name">Tenwick Media Limited<span>Tax services in the United Kingdom</span></div>
    <p class="abs np-desc">We here modify the site to improve the ranking by using the keywords contents.</p>
    <a class="abs np-more" href="#">view profile</a>
  </div>
  <div class="abs" style="left:6px;top:468px;width:380px;height:110px">
    <div class="np-photo" role="img" aria-label="Photo of two business people"></div>
    <div class="abs np-name">Tenwick Media Limited<span>Tax services in the United Kingdom</span></div>
    <p class="abs np-desc">We here modify the site to improve the ranking by using the keywords contents.</p>
    <a class="abs np-more" href="#">view profile</a>
  </div>
  <a class="abs small-link" href="#" style="left:0;top:640px">See the benifits</a>
  <a class="abs btn" href="#" style="left:189px;top:629px;width:186px;height:36px">LIST YOUR SERVICES</a>
</aside>

<aside class="abs knowledge">
  <h3 class="col-head">Knowledge Resource</h3>
  <p class="k-intro">Find resources for your business amongst</p>
  <ul class="k-list">
    <li><b>10,145</b> market analyses</li>
    <li><b>9,254</b> business tips</li>
    <li><b>3,215</b> agents and distributors</li>
    <li><b>50,145</b> service providers</li>
  </ul>
  <div class="k-select"><div class="box">Select a coutry</div><a class="ok" href="#">OK</a></div>
  <p class="k-pop">Most Popular</p>
  <p class="k-countries">China, Brazil, Japan, India, Egypt, Korea, Angola<br>Italy, England, Romania, Spain, Argentina, France,China,<br>Brazil, Japan, India, Egypt, Angola</p>
</aside>

<section class="abs partners" aria-label="Partner organisations">
  <div class="partner" style="width:76px;height:76px"></div>
  <div class="partner" style="width:90px"></div>
  <div class="partner" style="width:190px;height:44px"></div>
  <div class="partner" style="width:140px;height:50px"></div>
  <div class="partner" style="width:160px;height:40px"></div>
  <div class="partner" style="width:130px;height:56px"></div>
</section>

<footer class="abs footer">
  <div class="abs foot-col" style="left:42px"><h4>About</h4><ul><li>About Us</li><li>Partners</li><li>Site Map</li><li>Contact Us</li><li>Terms &amp; Conditions</li><li>Privacy Policy</li></ul></div>
  <div class="abs foot-col" style="left:231px"><h4>Most Popular Pages</h4><ul><li>Distributors</li><li>Country Risk</li><li>Tax Law</li><li>Market Research</li><li>Business Development</li><li>Mergers and Acqistions</li><li>Corporate Law</li></ul></div>
  <div class="abs foot-col" style="left:453px"><h4>For Importers/ Exporters</h4><ul><li>Import Export Services</li><li>Trade Companies, Agents</li><li>Market Analyses Worldwide</li><li>International Business Tips</li><li>Receive Offers for Services</li></ul></div>
  <div class="abs foot-col" style="left:711px"><h4>For Service Providers</h4><ul><li>Import Export Services</li><li>Trade Companies, Agents</li><li>Market Analyses Worldwide</li><li>International Business Tips</li><li>Receive Offers for Services</li></ul></div>
  <div class="abs foot-col" style="left:942px"><h4>Follow us</h4><ul class="social"><li><i></i>Chirpline</li><li><i></i>Linkwell</li><li><i></i>Folkpage</li><li><i></i>Searchly</li></ul></div>
  <div class="abs foot-rule"></div>
  <p class="abs copyright">© 2012 Company Name &nbsp;|&nbsp; All right reserved</p>
</footer>

</body>
</html>
```